Bref créative
Business Card for Business Advisory Firm
Marlowe Partners
Simple
Tom Brackett
Solutions Strategist
47 Pellham Road
Suite K
Boston, MA 02184
tbrackett@marlowepartners.example
www.marlowepartners.example
Somewhere on the front of the card I would like to list some of the services of the firm:
Project Support
Operations Analysis
Business Development
Would like a blue gingham pattern on entire back using the same colors as in the logo.
Layout guidelines: I will be using Zeb to print the cards. If there are any questions about layout for bleed etc, they can be found at link below:
http://us.zebprint.example/help/faq/templates-and-guidelines.html
Final, trimmed size
3.30" x 2.16"
84mm x 55mm
Full bleed size (recommended for creating finished artwork)
1039 x 697 pixels (300dpi)
3.46" x 2.32" (300dpi)
88mm x 59mm (300dpi)

```html
<!DOCTYPE html>
<html lang="en">
<head>
<meta charset="utf-8">
<title>Marlowe Partners – Business Cards</title>
<link rel="stylesheet" href="https://fonts.googleapis.com/css2?family=Arimo:wght@400;700&display=swap">
<style>
  :root {
    --brand-blue: #1f3a9e;
    --band-grey: #c9cbd1;
    --ink-grey: #7a7d86;
    --card-white: #ffffff;
    --backdrop: #eceef1;
  }
  * { box-sizing: border-box; margin: 0; padding: 0; }
  html, body { width: 1200px; height: 739px; overflow: hidden; }
  body {
    background: var(--backdrop);
    font-family: "Arimo", Arial, sans-serif;
    position: relative;
  }
  .card {
    position: absolute;
    top: 193px;
    width: 540px;
    height: 353px;
    background: var(--card-white);
    box-shadow: 0 4px 14px rgba(0,0,0,0.12);
    overflow: hidden;
  }
  .card--front { left: 40px; }
  .card--back { left: 620px; }

  /* Front card */
  .front-mark {
    position: absolute;
    left: 48px; top: 88px;
    width: 150px; height: 150px;
    background: var(--brand-blue);
  }
  .front-name {
    position: absolute;
    left: 226px; top: 92px;
    font-weight: 700;
    font-size: 30px;
    line-height: 1.05;
    color: var(--brand-blue);
  }
  .services {
    position: absolute;
    left: 240px; top: 176px;
    list-style: none;
    font-size: 15px;
    color: var(--ink-grey);
  }
  .services li {
    position: relative;
    padding-left: 22px;
    margin-bottom: 9px;
  }
  .services li::before {
    content: "";
    position: absolute;
    left: 2px; top: 5px;
    width: 7px; height: 7px;
    background: var(--brand-blue);
    transform: rotate(45deg);
  }

  /* Back card */
  .swoosh { position: absolute; inset: 0; }
  .holder {
    position: absolute;
    right: 250px; top: 22px;
    text-align: right;
  }
  .holder__name {
    font-size: 18px;
    font-weight: 700;
    color: var(--brand-blue);
  }
  .holder__title {
    font-size: 12px;
    color: var(--ink-grey);
    margin-top: 3px;
  }
  .back-brand {
    position: absolute;
    left: 40px; top: 134px;
    display: flex;
    align-items: center;
    gap: 12px;
  }
  .back-brand__square {
    width: 36px; height: 36px;
    background: var(--brand-blue);
  }
  .back-brand__name {
    font-size: 19px;
    font-weight: 700;
    color: var(--brand-blue);
  }
  .contact {
    position: absolute;
    right: 20px; top: 140px;
    list-style: none;
    text-align: right;
    font-size: 11px;
    line-height: 1.75;
    color: var(--card-white);
  }
  .contact li { display: flex; justify-content: flex-end; align-items: center; gap: 7px; white-space: nowrap; }
  .contact svg { width: 11px; height: 11px; fill: var(--card-white); flex: none; }
  .contact .spacer { width: 11px; flex: none; }
</style>
</head>
<body>

<section class="card card--front" aria-label="Card front">
  <div class="front-mark"></div>
  <div class="front-name">Marlowe Partners</div>
  <ul class="services">
    <li>Project Support</li>
    <li>Operations Analysis</li>
    <li>Business Development</li>
  </ul>
</section>

<section class="card card--back" aria-label="Card back">
  <svg class="swoosh" viewBox="0 0 540 353" width="540" height="353" aria-hidden="true">
    <path d="M540 8 C285 8 280 232 0 258 L0 353 L540 353 Z" fill="var(--band-grey)"/>
    <path d="M540 30 C300 30 300 250 0 280 L0 353 L540 353 Z" fill="var(--brand-blue)"/>
  </svg>

  <div class="holder">
    <div class="holder__name">Tom Brackett</div>
    <div class="holder__title">Solutions Strategist</div>
  </div>

  <div class="back-brand">
    <div class="back-brand__square"></div>
    <div class="back-brand__name">Marlowe Partners</div>
  </div>

  <ul class="contact">
    <li>617-555-0142
      <svg viewBox="0 0 24 24"><path d="M6.6 10.8a15 15 0 0 0 6.6 6.6l2.2-2.2c.3-.3.7-.4 1-.2 1.1.4 2.3.6 3.6.6.6 0 1 .4 1 1V20c0 .6-.4 1-1 1A17 17 0 0 1 3 4c0-.6.4-1 1-1h3.5c.6 0 1 .4 1 1 0 1.3.2 2.5.6 3.6.1.3 0 .7-.2 1z"/></svg>
    </li>
    <li>508-555-0187
      <svg viewBox="0 0 24 24"><path d="M7 2h10a2 2 0 0 1 2 2v16a2 2 0 0 1-2 2H7a2 2 0 0 1-2-2V4a2 2 0 0 1 2-2zm0 3v13h10V5z"/></svg>
    </li>
    <li>tbrackett@marlowepartners.example
      <svg viewBox="0 0 24 24"><path d="M3 5h18v14H3zm2 2v.4l7 4.6 7-4.6V7zm0 2.8V17h14V9.8l-7 4.6z"/></svg>
    </li>
    <li>www.marlowepartners.example
      <svg viewBox="0 0 24 24"><path d="M12 2a10 10 0 1 0 0 20 10 10 0 0 0 0-20zm0 2c.9 1.2 1.6 2.6 2 4h-4c.4-1.4 1.1-2.8 2-4zM4.3 14a8 8 0 0 1 0-4h3.4a16 16 0 0 0 0 4zm5.7 0a14 14 0 0 1 0-4h4a14 14 0 0 1 0 4zm6.3 0a16 16 0 0 0 0-4h3.4a8 8 0 0 1 0 4zm-6.3 2h4c-.4 1.4-1.1 2.8-2 4-.9-1.2-1.6-2.6-2-4z"/></svg>
    </li>
    <li>47 Pellham Road
      <svg viewBox="0 0 24 24"><path d="M12 2a7 7 0 0 0-7 7c0 5 7 13 7 13s7-8 7-13a7 7 0 0 0-7-7zm0 9.5A2.5 2.5 0 1 1 12 6.5a2.5 2.5 0 0 1 0 5z"/></svg>
    </li>
    <li>Suite K, Boston, MA 02184<span class="spacer"></span></li>
  </ul>
</section>

</body>
</html>
```